Business Card for Bright Furrow Lawn & Landscape

Double Sided Card Design - I think one side of the card should be cleaner, with logo, contact info, and "Complete Residential & Commercial Landscape Services", and on the other side it should list the services we offer:

- Lawn Care & Mowing
- Hedge & Shrub Trimming
- Leaf Removal & Clean Up
- Aeration & Sod
- Mulch & Rock Installations
- Landscape Installations & Renovations
- Commercial Snow Removal

Please make it clean and very professional... don't want it too be too busy, but want to tell them what we do.

Target Market(s)

Residential and Commercial

Industry/Entity Type

Landscape

Contact Information for Business Card

Fully Insured
Dale Ostrov
410-372-6184
Dostrov07@quillpost.net

Requirements
Must have
• Double Sided, Cleaner on one side, more information and text on the other side.

```html
<!DOCTYPE html>
<html lang="en">
<head>
<meta charset="utf-8">
<title>Bright Furrow Lawn &amp; Landscape – Business Card</title>
<link href="https://fonts.googleapis.com/css2?family=Cinzel:wght@400;500;600&display=swap" rel="stylesheet">
<style>
  :root {
    --stage: #d4d5d7;
    --charcoal: #262626;
    --leaf: #7ab648;
    --paper: #ffffff;
    --ink: #262626;
    --rule: #9a9a9a;
  }
  html, body {
    margin: 0;
    padding: 0;
    width: 1200px;
    height: 1000px;
    overflow: hidden;
    background: var(--stage);
    font-family: "Cinzel", "Times New Roman", serif;
  }
  .canvas { position: relative; width: 1200px; height: 1000px; }
  .card {
    position: absolute;
    left: 263px;
    width: 673px;
    height: 385px;
    overflow: hidden;
    box-shadow: 0 1px 4px rgba(0,0,0,0.25);
  }
  .card--front { top: 96px; background: var(--charcoal); }
  .card--back { top: 519px; background: var(--paper); }

  /* Front */
  .brand-mark {
    position: absolute;
    left: 110px; top: 32px;
    width: 80px; height: 80px;
    border-radius: 50%;
    background: var(--leaf);
  }
  .brand-name {
    position: absolute;
    left: 0; width: 300px; top: 140px;
    text-align: center;
    color: var(--leaf);
    font-size: 32px;
    font-weight: 500;
    line-height: 1;
    white-space: nowrap;
  }
  .brand-tagline {
    position: absolute;
    left: 0; width: 300px; top: 175px;
    text-align: center;
    color: var(--paper);
    font-size: 15px;
    font-weight: 500;
    letter-spacing: 3.5px;
    line-height: 1;
  }
  .divider {
    position: absolute;
    left: 22px; width: 256px; top: 217px;
    border-top: 1px dashed #bdbdbd;
  }
  .contact { position: absolute; left: 0; width: 300px; text-align: center; line-height: 1; white-space: nowrap; }
  .contact__name { top: 239px; color: var(--leaf); font-size: 25px; font-weight: 500; }
  .contact__phone { top: 268px; color: var(--paper); font-size: 27px; font-weight: 500; letter-spacing: 3px; }
  .contact__email { top: 307px; color: var(--paper); font-size: 14px; letter-spacing: 1px; }

  .photo-frame {
    position: absolute;
    left: 292px; top: 0;
    width: 400px; height: 352px;
  }
  .photo {
    position: absolute;
    left: 342px; top: 84px;
    width: 307px; height: 217px;
    border-radius: 40px;
    background: linear-gradient(180deg, #b9a58e 0%, #9fae84 45%, #5f9a36 72%, #3f7a22 100%);
  }
  .footer-band {
    position: absolute;
    left: 0; right: 0; bottom: 0;
    height: 33px;
    background: var(--leaf);
    color: var(--ink);
    font-size: 19.5px;
    font-weight: 600;
    letter-spacing: 0.6px;
    line-height: 33px;
    text-align: center;
    white-space: nowrap;
  }

  /* Back */
  .services-band {
    position: absolute;
    left: 0; right: 0; top: 43px;
    height: 286px;
    background: var(--charcoal);
  }
  .emblem {
    position: absolute;
    left: -18px; top: 22px;
    width: 340px; height: 340px;
    border-radius: 50%;
    background: var(--leaf);
  }
  .emblem-name {
    position: absolute;
    left: -18px; width: 340px; top: 177px;
    text-align: center;
    color: var(--paper);
    font-size: 30px;
    font-weight: 500;
    line-height: 1;
    white-space: nowrap;
  }
  .services-title {
    position: absolute;
    right: 16px; top: 51px;
    margin: 0;
    color: var(--paper);
    font-size: 29px;
    font-weight: 500;
    line-height: 1;
    white-space: nowrap;
  }
  .services-rule {
    position: absolute;
    left: 296px; right: 0; top: 86px;
    border-top: 1px dashed #cfcfcf;
  }
  .services-list {
    position: absolute;
    right: 16px; top: 117px;
    margin: 0; padding: 0;
    list-style: none;
    text-align: right;
    font-size: 18.5px;
    letter-spacing: 0.4px;
    line-height: 16px;
  }
  .services-list li { margin-bottom: 8.5px; }
  .services-list li:last-child { margin-top: 13px; }
  .services-list .accent { color: var(--leaf); }
  .services-list .plain { color: var(--paper); }
  .closing-rule {
    position: absolute;
    left: 296px; right: 0; top: 329px;
    border-top: 1px dashed var(--rule);
  }
  .insured {
    position: absolute;
    right: 14px; top: 355px;
    display: flex; align-items: center; gap: 10px;
    color: var(--ink);
    font-size: 22px;
    font-weight: 500;
    line-height: 1;
  }
  .insured svg { width: 22px; height: 22px; }
</style>
</head>
<body>
<main class="canvas">
  <section class="card card--front" aria-label="Card front">
    <span class="brand-mark" aria-hidden="true"></span>
    <div class="brand-name">Bright Furrow</div>
    <div class="brand-tagline">LAWN &amp; LANDSCAPE</div>
    <div class="divider"></div>
    <div class="contact contact__name">Dale Ostrov</div>
    <div class="contact contact__phone">410-372-6184</div>
    <div class="contact contact__email">DOSTROV07@QUILLPOST.NET</div>
    <div class="photo" role="img" aria-label="Photo of a push mower cutting fresh green grass with clippings flying"></div>
    <div class="footer-band">Complete Residential &amp; Commercial Landscape Services</div>
  </section>

  <section class="card card--back" aria-label="Card back">
    <div class="services-band"></div>
    <span class="emblem" aria-hidden="true"></span>
    <div class="emblem-name">Bright Furrow</div>
    <h2 class="services-title">The services we offer:</h2>
    <div class="services-rule"></div>
    <ul class="services-list">
      <li class="accent">Lawn Care &amp; Mowing</li>
      <li class="plain">Hedge &amp; Shrub Trimming</li>
      <li class="accent">Leaf Removal &amp; Clean Up</li>
      <li class="plain">Aeration &amp; Sod</li>
      <li class="accent">Mulch &amp; Rock Installations</li>
      <li class="plain">Landscape Installations &amp;<br>Renovations</li>
      <li class="accent">Commercial Snow Removal</li>
    </ul>
    <div class="closing-rule"></div>
    <div class="insured">
      <svg viewBox="0 0 22 22" aria-hidden="true">
        <rect x="1.5" y="3.5" width="17" height="17" fill="none" stroke="#262626" stroke-width="2"/>
        <path d="M5 11 L9.5 16 L20 2" fill="none" stroke="#262626" stroke-width="2.4"/>
      </svg>
      <span>Fully Insured</span>
    </div>
  </section>
</main>
</body>
</html>
```